Vehicle Rental Hire in the Algarve - Portugal

We are opening a Vehicle Rental company in the Algarve - Portugal - this will attract both locals and Tourists visiting. So we want this website to capture the beautiful location we will be set in, along with the familiarity of a vehicle rental company. And to keep a colour scheme in Line with out Logo. We are Fenmarel Vehicle Rental.

Industry/Entity Type

Vehicle Rental

Number of Pages Required

1 page

Requirements
Must have
• must be professional, and simple to use navigation bar - must also have a "make a reservation" box - similar to the screenshot attached - Under our logo it must read "Vehicle Rental"
Nice to have
• It needs to be in a colour scheme that fits in with our logo

```html
<!DOCTYPE html>
<html lang="en">
<head>
<meta charset="utf-8">
<title>Fenmarel Vehicle Rental</title>
<link href="https://fonts.googleapis.com/css2?family=Outfit:wght@300;400;500;600;700&family=Caveat:wght@400&display=swap" rel="stylesheet">
<style>
:root{
  --red:#d8302b;
  --ink:#111322;
  --muted:#6e7080;
  --lavender:#ebebf5;
  --card:#f3f3f8;
  --blue:#1b12d6;
  --blue-deep:#0d0b8e;
  --navy:#0c0a3c;
  --line:#e3e3ea;
  --white:#ffffff;
}
*{box-sizing:border-box;margin:0;padding:0}
html,body{width:1200px;height:4452px;overflow:hidden}
body{position:relative;font-family:'Outfit',sans-serif;color:var(--ink);background:var(--white)}
.abs{position:absolute}
.btn{position:absolute;background:var(--red);color:var(--white);border-radius:4px;font-size:12px;display:flex;align-items:center;justify-content:center}

/* hero */
.hero{position:absolute;left:0;top:0;width:1200px;height:524px;background:var(--lavender)}
.brand{position:absolute;left:173px;top:24px;display:flex;align-items:center;gap:8px}
.brand-dot{width:16px;height:16px;border-radius:50%;background:var(--blue)}
.brand-name{font-size:22px;font-weight:600;color:var(--blue)}
.brand-sub{position:absolute;left:197px;top:56px;font-size:11px;color:var(--red)}
.nav a{position:absolute;top:45px;font-size:12px;color:var(--ink);text-decoration:none}
.hero-title{position:absolute;left:173px;top:180px;font-size:47px;font-weight:600;line-height:58px;letter-spacing:-.3px}
.hero-tag{position:absolute;left:173px;top:318px;font-family:'Caveat',cursive;font-size:30px;color:var(--blue)}
.hero-car{position:absolute;left:620px;top:140px;width:580px;height:300px;border-radius:16px 0 0 16px;background:linear-gradient(135deg,#dcdde8 0%,#f7f7fb 40%,#c8cad6 75%,#9a9dab 100%)}
.badge{position:absolute;background:var(--white);border-radius:8px;box-shadow:0 6px 18px rgba(20,20,60,.08);padding:8px 14px}
.badge b{display:block;color:var(--red);font-weight:600}
.badge span{display:block;color:var(--ink)}

/* booking */
.booking{position:absolute;left:173px;top:463px;width:852px;height:111px;background:var(--white);border-radius:10px;box-shadow:0 10px 30px rgba(20,20,60,.09)}
.field label{position:absolute;top:26px;font-size:11px}
.field .box{position:absolute;top:50px;height:37px;border:1px solid var(--line);border-radius:5px;font-size:10px;color:var(--muted);display:flex;align-items:center;padding-left:12px;gap:8px;white-space:nowrap}

/* picks */
.section-title{position:absolute;font-size:28px;font-weight:600}
.section-sub{position:absolute;font-size:11px;color:var(--muted)}
.car{position:absolute;width:268px;height:360px}
.car .photo{width:268px;height:230px;border-radius:8px}
.car .name{position:absolute;top:252px;font-size:13px;font-weight:600}
.car .rate{position:absolute;right:0;top:252px;font-size:11px;color:var(--muted)}
.car .rate i{font-style:normal;color:#f5b400}
.car .spec{position:absolute;top:273px;font-size:10px;color:var(--muted)}
.car .spec2{position:absolute;top:294px;font-size:9px;color:var(--muted)}
.car hr{position:absolute;top:332px;width:268px;border:0;border-top:1px solid var(--line)}
.car .from{position:absolute;top:347px;font-size:9px;color:var(--muted)}
.car .price{position:absolute;right:0;top:343px;font-size:13px;font-weight:600}

/* about */
.about{position:absolute;left:0;top:1653px;width:1200px;height:574px;background:linear-gradient(120deg,var(--blue-deep),var(--blue) 60%,#1e18e8)}
.about h2{position:absolute;left:173px;top:140px;font-size:29px;font-weight:600;line-height:36px;color:var(--white)}
.about p{position:absolute;left:173px;top:240px;width:340px;font-size:11px;line-height:21px;color:#dcdcff}
.about-blob{position:absolute;left:570px;top:130px;width:230px;height:270px;border-radius:50%;background:#2c6fe3}
.about-photo{position:absolute;left:622px;top:93px;width:320px;height:343px;border-radius:50%;background:radial-gradient(circle at 45% 40%,#d9c7b8,#8aa1b8 55%,#4d6b8f)}

/* testimonials */
.say-title{position:absolute;left:173px;top:2346px;font-size:30px;font-weight:600;line-height:36px}
.say-sub{position:absolute;left:173px;top:2483px;width:190px;font-size:10px;line-height:21px;color:var(--muted)}
.arrow{position:absolute;top:2573px;width:40px;height:40px;border-radius:50%;background:#ececf2;display:flex;align-items:center;justify-content:center}
.review{position:absolute;top:2308px;width:268px}
.review .photo{height:147px;border-radius:6px}
.review h4{margin-top:26px;font-size:13px;font-weight:600}
.review p{margin-top:10px;font-size:10px;line-height:21px;color:var(--muted)}
.review .who{position:absolute;top:314px;font-size:11px;font-weight:600}
.review .where{position:absolute;top:334px;font-size:9px;color:var(--muted)}
.review .quote{position:absolute;right:14px;top:306px;font-size:48px;line-height:40px;color:#d7d7ea;font-weight:700}

/* why */
.why{position:absolute;left:0;top:2732px;width:1200px;height:709px;background:#f3f3f9}
.why-item{position:absolute;top:210px;width:200px;text-align:center}
.why-icon{width:76px;height:76px;margin:0 auto;border-radius:50%;background:var(--white);display:flex;align-items:center;justify-content:center;box-shadow:0 6px 16px rgba(20,20,80,.06)}
.why-item h4{margin-top:28px;font-size:16px;font-weight:600}
.why-item p{margin-top:18px;font-size:10px;line-height:21px;color:var(--muted)}
.why-scene{position:absolute;left:0;top:432px;width:1200px;height:277px;background:linear-gradient(180deg,#f3f3f9 0%,#dfe3ea 55%,#7f9a5a 88%,#3f6a2a 100%)}

/* faq */
.faq{position:absolute;left:245px;width:710px}
.faq-item{position:absolute;left:0;width:710px;border-bottom:1px solid var(--line)}
.faq-item h5{font-size:13px;font-weight:500}
.faq-item p{margin-top:14px;font-size:10px;line-height:21px;color:var(--muted);width:640px}
.faq-toggle{position:absolute;right:0;top:0;width:18px;height:18px;border:1.3px solid var(--ink);border-radius:50%;display:flex;align-items:center;justify-content:center}

/* footer */
.footer{position:absolute;left:0;top:4075px;width:1200px;height:377px;background:var(--navy);color:#b9b9d4}
.footer h6{position:absolute;top:83px;font-size:11px;font-weight:600;color:var(--white)}
.footer a{position:absolute;font-size:11px;color:#b9b9d4;text-decoration:none}
.footer .copy{position:absolute;left:0;width:1200px;top:338px;text-align:center;font-size:11px}
</style>
</head>
<body>

<header class="hero">
  <div class="brand"><span class="brand-dot"></span><span class="brand-name">Fenmarel</span></div>
  <div class="brand-sub">Vehicle Rental</div>
  <nav class="nav">
    <a style="left:443px">Home</a>
    <a style="left:513px">Our Cars</a>
    <a style="left:602px">About Us</a>
    <a style="left:692px">Contact Us</a>
    <a style="left:877px">Login</a>
  </nav>
  <div class="btn" style="left:937px;top:33px;width:88px;height:38px">Sign Up</div>

  <h1 class="hero-title">Hassle Free Car<br>Rental in Portugal</h1>
  <div class="hero-tag">Take a Rent for Your Every Journey</div>

  <div class="hero-car" role="img" aria-label="White electric sedan, front three-quarter view"></div>
  <div class="badge" style="left:785px;top:116px;width:112px">
    <b style="font-size:17px">500</b><span style="font-size:10px">Car Available</span>
  </div>
  <div class="badge" style="left:660px;top:190px;width:100px;padding:6px 10px">
    <b style="font-size:9px">5 Star</b><span style="font-size:7px">Customer Ratings</span>
  </div>
</header>

<section class="booking">
  <div class="field">
    <label style="left:27px">Collect From</label>
    <div class="box" style="left:27px;width:160px">
      <svg width="11" height="13" viewBox="0 0 11 13"><path d="M5.5 12S1 7.5 1 5a4.5 4.5 0 0 1 9 0c0 2.5-4.5 7-4.5 7z" fill="none" stroke="#8a8c99"/><circle cx="5.5" cy="5" r="1.5" fill="none" stroke="#8a8c99"/></svg>City, Location</div>
    <label style="left:195px">Drop To</label>
    <div class="box" style="left:195px;width:159px">
      <svg width="11" height="13" viewBox="0 0 11 13"><path d="M5.5 12S1 7.5 1 5a4.5 4.5 0 0 1 9 0c0 2.5-4.5 7-4.5 7z" fill="none" stroke="#8a8c99"/><circle cx="5.5" cy="5" r="1.5" fill="none" stroke="#8a8c99"/></svg>City, Location</div>
    <label style="left:361px">Collect Date &amp; Time</label>
    <div class="box" style="left:361px;width:185px">
      <svg width="11" height="13" viewBox="0 0 11 13"><path d="M5.5 12S1 7.5 1 5a4.5 4.5 0 0 1 9 0c0 2.5-4.5 7-4.5 7z" fill="none" stroke="#8a8c99"/><circle cx="5.5" cy="5" r="1.5" fill="none" stroke="#8a8c99"/></svg>14 Apr, 2024 &nbsp;|&nbsp; 10:30 AM
      <svg width="9" height="6" viewBox="0 0 9 6"><path d="M1 1l3.5 3.5L8 1" fill="none" stroke="#333"/></svg></div>
    <label style="left:555px">Drop Date &amp; Time</label>
    <div class="box" style="left:555px;width:185px">
      <svg width="11" height="13" viewBox="0 0 11 13"><path d="M5.5 12S1 7.5 1 5a4.5 4.5 0 0 1 9 0c0 2.5-4.5 7-4.5 7z" fill="none" stroke="#8a8c99"/><circle cx="5.5" cy="5" r="1.5" fill="none" stroke="#8a8c99"/></svg>14 Apr, 2024 &nbsp;|&nbsp; 10:30 AM
      <svg width="9" height="6" viewBox="0 0 9 6"><path d="M1 1l3.5 3.5L8 1" fill="none" stroke="#333"/></svg></div>
  </div>
  <div class="btn" style="left:750px;top:50px;width:75px;height:37px">Go</div>
</section>

<h2 class="section-title" style="left:173px;top:650px">Top Picks Vehicle This Month</h2>
<p class="section-sub" style="left:173px;top:696px">It is a long established fact that a reader will be distracted by the readable content of a page</p>

<div class="car" style="left:173px;top:747px">
  <div class="photo" role="img" aria-label="Bronze hatchback car" style="background:radial-gradient(ellipse at 50% 55%,#b9a57f 0%,#d9d0c0 40%,var(--card) 75%)"></div>
  <div class="name">Asterio</div><div class="rate"><i>★</i> 4.7</div>
  <div class="spec">Automatic / Manual</div><div class="spec2">Seat 4 &nbsp;&nbsp;&nbsp;&nbsp;&nbsp;&nbsp;&nbsp;&nbsp;&nbsp; Airbag 1</div>
  <hr><div class="from">Start From</div><div class="price">€70/ Day</div>
</div>
<div class="car" style="left:465px;top:747px">
  <div class="photo" role="img" aria-label="Black sports coupe" style="background:radial-gradient(ellipse at 50% 55%,#3a3a3e 0%,#a9a9b0 40%,var(--card) 75%)"></div>
  <div class="name">Asterio</div><div class="rate"><i>★</i> 4.7</div>
  <div class="spec">Automatic / Manual</div><div class="spec2">Seat 4 &nbsp;&nbsp;&nbsp;&nbsp;&nbsp;&nbsp;&nbsp;&nbsp;&nbsp; Airbag 1</div>
  <hr><div class="from">Start From</div><div class="price">€70/ Day</div>
</div>
<div class="car" style="left:757px;top:747px">
  <div class="photo" role="img" aria-label="Black pickup truck" style="background:radial-gradient(ellipse at 50% 50%,#2e2e32 0%,#a4a4ab 42%,var(--card) 75%)"></div>
  <div class="name">Asterio</div><div class="rate"><i>★</i> 4.7</div>
  <div class="spec">Automatic / Manual</div><div class="spec2">Seat 4 &nbsp;&nbsp;&nbsp;&nbsp;&nbsp;&nbsp;&nbsp;&nbsp;&nbsp; Airbag 1</div>
  <hr><div class="from">Start From</div><div class="price">€70/ Day</div>
</div>
<div class="car" style="left:173px;top:1145px">
  <div class="photo" role="img" aria-label="Red classic muscle car with white stripes" style="background:radial-gradient(ellipse at 50% 55%,#d8373a 0%,#e9b6b7 40%,var(--card) 75%)"></div>
  <div class="name">Asterio</div><div class="rate"><i>★</i> 4.7</div>
  <div class="spec">Automatic / Manual</div><div class="spec2">Seat 4 &nbsp;&nbsp;&nbsp;&nbsp;&nbsp;&nbsp;&nbsp;&nbsp;&nbsp; Airbag 1</div>
  <hr><div class="from">Start From</div><div class="price">€70/ Day</div>
</div>
<div class="car" style="left:465px;top:1145px">
  <div class="photo" role="img" aria-label="White SUV" style="background:radial-gradient(ellipse at 50% 50%,#9c9ea6 0%,#d6d7dd 40%,var(--card) 75%)"></div>
  <div class="name">Asterio</div><div class="rate"><i>★</i> 4.7</div>
  <div class="spec">Automatic / Manual</div><div class="spec2">Seat 4 &nbsp;&nbsp;&nbsp;&nbsp;&nbsp;&nbsp;&nbsp;&nbsp;&nbsp; Airbag 1</div>
  <hr><div class="from">Start From</div><div class="price">€70/ Day</div>
</div>
<div class="car" style="left:757px;top:1145px">
  <div class="photo" role="img" aria-label="Blue classic convertible" style="background:radial-gradient(ellipse at 50% 55%,#2f66c4 0%,#b4c7e8 40%,var(--card) 75%)"></div>
  <div class="name">Asterio</div><div class="rate"><i>★</i> 4.7</div>
  <div class="spec">Automatic / Manual</div><div class="spec2">Seat 4 &nbsp;&nbsp;&nbsp;&nbsp;&nbsp;&nbsp;&nbsp;&nbsp;&nbsp; Airbag 1</div>
  <hr><div class="from">Start From</div><div class="price">€70/ Day</div>
</div>

<div class="btn" style="left:538px;top:1556px;width:124px;height:36px">View All</div>

<section class="about">
  <h2>Vehicle Rental company<br>in the Algarve - Portugal</h2>
  <p>Lorem Ipsum is simply dummy text of the printing and typesetting industry. Lorem Ipsum has been the industry's standard dummy text ever since the 1500s, when an unknown printer took a galley of type and scrambled it to make a type specimen book. It has survived not only five centuries, but also the leap into electronic typesetting, remaining</p>
  <div class="btn" style="left:173px;top:399px;width:123px;height:36px;font-size:11px">Learn More</div>
  <div class="about-blob"></div>
  <div class="about-photo" role="img" aria-label="Family with a dog leaning out of a silver car window"></div>
</section>

<h2 class="say-title">What Our<br>Customer Say<br>About Us</h2>
<p class="say-sub">It is a long established fact that a reader will be distracted by the readable</p>
<div class="arrow" style="left:174px"><svg width="14" height="12" viewBox="0 0 14 12"><path d="M13 6H1M6 1L1 6l5 5" fill="none" stroke="#111322" stroke-width="1.5"/></svg></div>
<div class="arrow" style="left:222px"><svg width="14" height="12" viewBox="0 0 14 12"><path d="M1 6h12M8 1l5 5-5 5" fill="none" stroke="#111322" stroke-width="1.5"/></svg></div>

<article class="review" style="left:450px">
  <div class="photo" role="img" aria-label="Two friends relaxing in a blue convertible" style="background:linear-gradient(160deg,#9fc3e6,#e6d2b8 60%,#3b77c9)"></div>
  <h4>Very simple to rent the car</h4>
  <p>Lorem Ipsum is simply dummy text of the printing and typesetting industry. Lorem Ipsum has been the industry's standard dummy text ever since the 1500s</p>
  <div class="who">Tomas Valera</div><div class="where">Algarve - Portugal</div><div class="quote">”</div>
</article>
<article class="review" style="left:757px">
  <div class="photo" role="img" aria-label="Friends driving in an open car" style="background:linear-gradient(160deg,#a7c97a,#e7dccb 55%,#b9c0c8)"></div>
  <h4>Very simple to rent the car</h4>
  <p>Lorem Ipsum is simply dummy text of the printing and typesetting industry. Lorem Ipsum has been the industry's standard dummy text ever since the 1500s</p>
  <div class="who">Tomas Valera</div><div class="where">Algarve - Portugal</div><div class="quote">”</div>
</article>

<section class="why">
  <h2 class="section-title" style="left:0;width:1200px;text-align:center;top:80px">Why You Choose Us</h2>
  <p class="section-sub" style="left:0;width:1200px;text-align:center;top:126px">It is a long established fact that a reader will be distracted by the readable</p>
  <div class="why-item" style="left:171px">
    <div class="why-icon"><svg width="30" height="30" viewBox="0 0 30 30"><circle cx="15" cy="12" r="9" fill="#1b12d6"/><text x="15" y="16" font-size="11" text-anchor="middle" fill="#fff" font-family="Outfit,sans-serif">$</text><path d="M15 23v5M12 26l3 3 3-3" stroke="#1b12d6" stroke-width="2" fill="none"/></svg></div>
    <h4>Low Pricing</h4><p>Lorem Ipsum is simply dummy text of the printing and typesetting industry rem Ipsum has</p>
  </div>
  <div class="why-item" style="left:391px">
    <div class="why-icon"><svg width="32" height="30" viewBox="0 0 32 30"><path d="M16 6l3 6 6 1-4.5 4 1 6L16 20l-5.5 3 1-6L7 13l6-1z" fill="#1b12d6"/><path d="M5 6a14 14 0 0 0 0 18M27 6a14 14 0 0 1 0 18" stroke="#1b12d6" stroke-width="2" fill="none"/></svg></div>
    <h4>High Quality</h4><p>Lorem Ipsum is simply dummy text of the printing and typesetting industry rem Ipsum has</p>
  </div>
  <div class="why-item" style="left:609px">
    <div class="why-icon"><svg width="26" height="30" viewBox="0 0 26 30"><path d="M13 2l10 4v8c0 7-5 12-10 14C8 26 3 21 3 14V6z" fill="#1b12d6"/><path d="M8 15l4 4 6-7" stroke="#fff" stroke-width="2" fill="none"/></svg></div>
    <h4>Clean &amp; Safe</h4><p>Lorem Ipsum is simply dummy text of the printing and typesetting industry rem Ipsum has</p>
  </div>
  <div class="why-item" style="left:828px">
    <div class="why-icon"><svg width="30" height="30" viewBox="0 0 30 30"><path d="M15 2l3 3 4-1 1 4 4 1-1 4 3 2-3 2 1 4-4 1-1 4-4-1-3 3-3-3-4 1-1-4-4-1 1-4-3-2 3-2-1-4 4-1 1-4 4 1z" fill="#1b12d6"/><text x="15" y="19" font-size="11" text-anchor="middle" fill="#fff" font-family="Outfit,sans-serif">%</text></svg></div>
    <h4>Best Discounts</h4><p>Lorem Ipsum is simply dummy text of the printing and typesetting industry rem Ipsum has</p>
  </div>
  <div class="why-scene" role="img" aria-label="White SUV parked on grass beside a family walking together"></div>
</section>

<h2 class="section-title" style="left:0;width:1200px;text-align:center;top:3516px">Frequently Asked Questions</h2>
<p class="section-sub" style="left:0;width:1200px;text-align:center;top:3564px">It is a long established fact that a reader will be distracted by the readable</p>

<section class="faq" style="top:3614px">
  <div class="faq-item" style="top:0;height:124px">
    <h5>Lorem Ipsum is simply dummy text of the printing?</h5>
    <p>Lorem Ipsum is simply dummy text of the printing and typesetting industry. Lorem Ipsum has been the industry's standard dummy text ever since the 1500s, when an unknown printer took a galley of type and scrambled it to make a type specimen book.</p>
    <div class="faq-toggle"><svg width="8" height="5" viewBox="0 0 8 5"><path d="M1 4l3-3 3 3" fill="none" stroke="#111322" stroke-width="1.2"/></svg></div>
  </div>
  <div class="faq-item" style="top:147px;height:55px">
    <h5>It is a long established fact that a reader will be distracted?</h5>
    <div class="faq-toggle"><svg width="8" height="5" viewBox="0 0 8 5"><path d="M1 1l3 3 3-3" fill="none" stroke="#111322" stroke-width="1.2"/></svg></div>
  </div>
  <div class="faq-item" style="top:216px;height:55px">
    <h5>Many desktop publishing packages and web page?</h5>
    <div class="faq-toggle"><svg width="8" height="5" viewBox="0 0 8 5"><path d="M1 1l3 3 3-3" fill="none" stroke="#111322" stroke-width="1.2"/></svg></div>
  </div>
  <div class="faq-item" style="top:286px;height:55px">
    <h5>There are many variations of passages of Lorem Ipsum available?</h5>
    <div class="faq-toggle"><svg width="8" height="5" viewBox="0 0 8 5"><path d="M1 1l3 3 3-3" fill="none" stroke="#111322" stroke-width="1.2"/></svg></div>
  </div>
  <div class="faq-item" style="top:355px;height:30px;border-bottom:0">
    <h5>The standard chunk of Lorem Ipsum used since the 1500s is reproduced below for those?</h5>
    <div class="faq-toggle"><svg width="8" height="5" viewBox="0 0 8 5"><path d="M1 1l3 3 3-3" fill="none" stroke="#111322" stroke-width="1.2"/></svg></div>
  </div>
</section>

<footer class="footer">
  <div class="brand" style="top:100px"><span class="brand-dot" style="background:#3a34ff"></span><span class="brand-name" style="color:#4c46ff">Fenmarel</span></div>
  <div class="brand-sub" style="top:132px">Vehicle Rental</div>
  <p class="abs" style="left:173px;top:176px;width:210px;font-size:10px;line-height:21px">Lorem Ipsum is simply dummy text of the printing and typesetting industry.</p>

  <h6 style="left:463px">Quick Links</h6>
  <a style="left:463px;top:117px">Home</a>
  <a style="left:463px;top:150px">Our Cars</a>
  <a style="left:463px;top:182px">About Us</a>
  <a style="left:463px;top:215px">Contact Us</a>

  <h6 style="left:610px">Support</h6>
  <a style="left:610px;top:117px">Contact Us</a>
  <a style="left:610px;top:150px">Faq's</a>
  <a style="left:610px;top:182px">Terms &amp; Condition</a>

  <h6 style="left:776px">Get Updates</h6>
  <div class="abs" style="left:776px;top:118px;width:160px;height:38px;border:1px solid #2a2862;border-radius:4px 0 0 4px;font-size:11px;display:flex;align-items:center;padding-left:14px">Enter Your Email</div>
  <div class="btn" style="left:936px;top:118px;width:89px;height:38px">Subscribe</div>

  <div class="copy">Copyright © 2024 Fenmarel. All Rights Reserved</div>
</footer>

</body>
</html>
```